Copperleaf Motorized Shade Business Card

Hello, we've had our logo made. Now we are looking for a clean and cool looking business card. One side can just be the logo with any design elements that might look good with it. The other side will be Name, Phone Number and Email. There will not be an address on the card.

```html
<!DOCTYPE html>
<html lang="en">
<head>
<meta charset="utf-8">
<title>Copperleaf Motorized Shade Business Card</title>
<link href="https://fonts.googleapis.com/css2?family=Oswald:wght@500;600&family=Open+Sans:wght@400&display=swap" rel="stylesheet">
<style>
  :root {
    --navy: #0e3a78;
    --sky: #1aa6e8;
    --white: #ffffff;
    --ink: #1c2230;
    --rule: #5a5f6a;
    --backdrop: #e6e8ec;
  }
  * { margin: 0; padding: 0; box-sizing: border-box; }
  html, body {
    width: 1200px;
    height: 800px;
    overflow: hidden;
    background: var(--backdrop);
  }
  .canvas {
    position: relative;
    width: 1200px;
    height: 800px;
  }
  .card {
    position: absolute;
    width: 540px;
    height: 309px;
    overflow: hidden;
    box-shadow: 0 10px 30px rgba(0, 0, 0, 0.18);
  }
  .card::after {
    content: "";
    position: absolute;
    left: 0;
    right: 0;
    bottom: 0;
    height: 8px;
    background: var(--sky);
  }
  .card-front {
    left: 45px;
    top: 110px;
    background: var(--navy);
    display: flex;
    align-items: center;
    justify-content: center;
  }
  .card-back {
    left: 615px;
    top: 380px;
    background: var(--white);
  }
  .brand {
    display: flex;
    align-items: center;
    gap: 14px;
  }
  .brand-mark {
    width: 34px;
    height: 34px;
    flex: none;
  }
  .brand-name {
    font-family: "Oswald", sans-serif;
    font-weight: 600;
    text-transform: uppercase;
    line-height: 1.05;
  }
  .brand-name .line-main {
    display: block;
    font-size: 44px;
    letter-spacing: 1px;
  }
  .brand-name .line-sub {
    display: block;
    font-size: 15px;
    letter-spacing: 5px;
  }
  .card-front .brand-mark { background: var(--sky); }
  .card-front .brand-name { color: var(--white); }

  .card-back .brand {
    position: absolute;
    left: 305px;
    top: 92px;
    gap: 10px;
  }
  .card-back .brand-mark { width: 26px; height: 26px; background: var(--sky); }
  .card-back .brand-name { color: var(--navy); }
  .card-back .brand-name .line-main { font-size: 36px; }
  .card-back .brand-name .line-sub { font-size: 12px; letter-spacing: 4px; }

  .divider {
    position: absolute;
    left: 285px;
    top: 72px;
    width: 1px;
    height: 150px;
    background: var(--rule);
  }
  .contact {
    position: absolute;
    right: 275px;
    top: 82px;
    text-align: right;
  }
  .person-name {
    font-family: "Oswald", sans-serif;
    font-weight: 600;
    font-size: 34px;
    line-height: 1;
    text-transform: uppercase;
    letter-spacing: 0.5px;
  }
  .person-name .first { color: var(--navy); }
  .person-name .last { color: var(--sky); }
  .person-role {
    font-family: "Open Sans", sans-serif;
    font-size: 14px;
    color: var(--ink);
    margin-top: 4px;
  }
  .details {
    list-style: none;
    margin-top: 30px;
    font-family: "Open Sans", sans-serif;
    font-size: 14px;
    color: var(--ink);
  }
  .details li {
    display: flex;
    align-items: center;
    justify-content: flex-end;
    gap: 10px;
    margin-top: 6px;
  }
  .details svg {
    width: 14px;
    height: 14px;
    flex: none;
  }
</style>
</head>
<body>
<main class="canvas">
  <section class="card card-front" aria-label="Card front">
    <div class="brand">
      <span class="brand-mark" aria-hidden="true"></span>
      <p class="brand-name">
        <span class="line-main">Copperleaf</span>
        <span class="line-sub">Motorized Shade</span>
      </p>
    </div>
  </section>

  <section class="card card-back" aria-label="Card back">
    <div class="contact">
      <h1 class="person-name"><span class="first">Daniel</span> <span class="last">Reeve</span></h1>
      <p class="person-role">Director</p>
      <ul class="details">
        <li>
          <span>000 000 0000</span>
          <svg viewBox="0 0 16 16" aria-hidden="true">
            <path d="M4 1.5c-1.2.6-2.2 1.6-2.2 3 0 4.6 5.1 9.7 9.7 9.7 1.4 0 2.4-1 3-2.2L11.7 10l-2 1.3C7.6 10.3 5.7 8.4 4.7 6.3L6 4.3 4 1.5z" fill="none" stroke="#1aa6e8" stroke-width="1.4" stroke-linejoin="round"/>
          </svg>
        </li>
        <li>
          <span>info@yourmail.com.au</span>
          <svg viewBox="0 0 16 16" aria-hidden="true">
            <rect x="1.5" y="3.5" width="13" height="9" fill="none" stroke="#1aa6e8" stroke-width="1.3"/>
            <path d="M1.5 3.5 8 9l6.5-5.5" fill="none" stroke="#1aa6e8" stroke-width="1.3"/>
          </svg>
        </li>
      </ul>
    </div>
    <span class="divider" aria-hidden="true"></span>
    <div class="brand">
      <span class="brand-mark" aria-hidden="true"></span>
      <p class="brand-name">
        <span class="line-main">Copperleaf</span>
        <span class="line-sub">Motorized Shade</span>
      </p>
    </div>
  </section>
</main>
</body>
</html>
```